Interior Decorating and Event Styling Business Card Design

We need a business card design for a bespoke interior decorating and event styling business, mostly weddings. We also do custom paint finishes and painted floor finishes. We want something simple, organic and stylish with good colour tones used.

On our card we would like our services listed like so -

Interior Decorating
Wedding and Event Styling
Bespoke furniture paint finishes
Painted floor finishes

Industry/Entity Type

Paint

Contact Information for Business Card

Mabel & Moss Design
Rosalind 0487315026
Petra 0439572604
rosalind.carver@mailbrook.com.au
petraloom@tmv4.com.au

```html
<!DOCTYPE html>
<html lang="en">
<head>
<meta charset="utf-8">
<title>Mabel &amp; Moss Design – Business Cards</title>
<link rel="stylesheet" href="https://fonts.googleapis.com/css2?family=Alegreya:ital,wght@0,400;0,700;1,400;1,700&family=Open+Sans:wght@400&display=swap">
<style>
  :root {
    --backdrop: #ebebe8;
    --teal: #13988d;
    --teal-deep: #0d8a80;
    --teal-light: #1aa89b;
    --mint: #e4eeea;
    --mint-soft: #d9e6e1;
    --ink-grey: #4a4d4c;
    --white: #ffffff;
  }
  * { margin: 0; padding: 0; box-sizing: border-box; }
  html, body {
    width: 1200px;
    height: 784px;
    overflow: hidden;
    background: var(--backdrop);
  }
  .sheet {
    position: relative;
    width: 1200px;
    height: 784px;
  }
  .card {
    position: absolute;
    top: 242px;
    width: 540px;
    height: 300px;
    box-shadow: 0 6px 18px rgba(0,0,0,0.12);
    overflow: hidden;
  }

  /* Services side */
  .card--services {
    left: 40px;
    background: linear-gradient(180deg, var(--teal-light) 0%, var(--teal) 45%, var(--teal-deep) 100%);
    color: var(--white);
    text-align: center;
    font-family: "Alegreya", Georgia, serif;
  }
  .services-brand {
    margin-top: 34px;
    font-size: 24px;
    font-weight: 400;
    letter-spacing: 1px;
  }
  .services-list {
    list-style: none;
    margin-top: 26px;
    font-style: italic;
    font-size: 24px;
    line-height: 1.22;
  }

  /* Contact side */
  .card--contact {
    left: 620px;
    background: var(--mint);
    font-family: "Alegreya", Georgia, serif;
  }
  .damask-field {
    position: absolute;
    inset: 0;
    background: radial-gradient(ellipse at 50% 45%, var(--mint) 0%, var(--mint-soft) 100%);
  }
  .frame {
    position: absolute;
    inset: 12px;
    border: 5px solid var(--teal);
  }
  .brand {
    position: absolute;
    top: 62px;
    left: 0;
    width: 100%;
    text-align: center;
  }
  .brand-name {
    font-size: 40px;
    font-weight: 400;
    color: var(--teal);
    line-height: 1;
  }
  .brand-tag {
    margin-top: 6px;
    font-size: 22px;
    font-weight: 400;
    color: var(--teal);
    letter-spacing: 18px;
    padding-left: 18px;
  }
  .contact {
    position: absolute;
  }
  .contact-name {
    font-weight: 700;
    color: var(--teal);
    line-height: 1.1;
  }
  .contact-phone {
    font-family: "Open Sans", Arial, sans-serif;
    color: var(--ink-grey);
    line-height: 1.35;
  }
  .contact-email {
    font-style: italic;
    color: var(--ink-grey);
    line-height: 1.3;
  }
  .contact--petra {
    right: 34px;
    top: 160px;
    text-align: right;
  }
  .contact--petra .contact-name { font-size: 17px; }
  .contact--petra .contact-phone { font-size: 13px; }
  .contact--petra .contact-email { font-size: 14px; margin-top: 14px; }
  .contact--rosalind {
    left: 34px;
    bottom: 30px;
  }
  .contact--rosalind .contact-name { font-size: 21px; }
  .contact--rosalind .contact-phone { font-size: 16px; }
  .contact--rosalind .contact-email { font-size: 17px; }
</style>
</head>
<body>
  <main class="sheet">
    <section class="card card--services" aria-label="Services side">
      <p class="services-brand">Mabel &amp; Moss Design</p>
      <ul class="services-list">
        <li>Interior Decorating</li>
        <li>Wedding and Event Styling</li>
        <li>Bespoke furniture paint finishes</li>
        <li>Painted floor finishes</li>
      </ul>
    </section>

    <section class="card card--contact" aria-label="Contact side">
      <div class="damask-field" role="img" aria-label="Faint mint damask floral pattern background"></div>
      <div class="frame"></div>
      <div class="brand">
        <p class="brand-name">Mabel &amp; Moss</p>
        <p class="brand-tag">DESIGN</p>
      </div>
      <div class="contact contact--petra">
        <p class="contact-name">Petra</p>
        <p class="contact-phone">0439572604</p>
        <p class="contact-email">petraloom@tmv4.com.au</p>
      </div>
      <div class="contact contact--rosalind">
        <p class="contact-name">Rosalind</p>
        <p class="contact-phone">0487315026</p>
        <p class="contact-email">rosalind.carver@mailbrook.com.au</p>
      </div>
    </section>
  </main>
</body>
</html>
```